TIVARELCAP web-presence redisign

We would like to have our existing web-presence redesigned. Have a look at www.tivarel.ch (please use explorer). To the existing 11 pages we would add one more.

```html
<!DOCTYPE html>
<html lang="de">
<head>
<meta charset="utf-8">
<title>TIVARELCAP Zahnarztpraxis</title>
<link rel="stylesheet" href="https://fonts.googleapis.com/css2?family=Arimo:wght@400;700&family=Libre+Baskerville&family=Oswald:wght@400&family=Roboto+Condensed:wght@400;700&family=Open+Sans:wght@400;600&family=Raleway:wght@400;600&display=swap">
<style>
:root{
  --header-bg:#dcdcdc;
  --strip-bg:#e4e4e4;
  --orange:#e0a23c;
  --orange-text:#d08a2a;
  --ink:#3d3d3d;
  --soft-bg:#f1f1f1;
  --footer-bg:#2b2b2b;
  --bottom-bg:#121212;
}
*{box-sizing:border-box;margin:0;padding:0}
html,body{width:1047px;height:1200px;overflow:hidden}
body{position:relative;font-family:"Arimo",Arial,sans-serif;color:var(--ink);background:#fff}
.abs{position:absolute}
.site-header{left:0;top:0;width:1047px;height:97px;background:var(--header-bg);border-bottom:1px solid #c8c8c8}
.brand{left:92px;top:34px;font-family:"Libre Baskerville",Georgia,serif;font-size:26px;line-height:28px;color:#9a7a30;display:flex;align-items:center;gap:10px}
.brand-mark{width:14px;height:14px;background:var(--orange)}
.brand small{display:block;font-size:20px}
.social-top{right:84px;top:9px;display:flex;gap:7px}
.social-top span{width:28px;height:28px;border:2px solid #9a9a9a;border-radius:50%}
.main-nav{left:515px;top:61px;display:flex;font-family:"Raleway",sans-serif;font-weight:600;font-size:11.5px;color:#444}
.main-nav a{padding:8px 12px;margin-right:14px;color:inherit;text-decoration:none}
.main-nav a.active{background:linear-gradient(#f2b54a,#dd922a);color:#fff;border:1px solid #c9801f}
.hero{left:0;top:97px;width:1047px;height:328px;background:linear-gradient(180deg,#f1c05f 0%,#e3a444 55%,#c98434 100%)}
.hero-photo{left:545px;top:0;width:502px;height:328px;background:radial-gradient(ellipse at 55% 45%,#f1d3bd 0%,#e3b08a 35%,rgba(224,162,68,0) 70%)}
.hero-title{left:100px;top:52px;font-family:"Libre Baskerville",Georgia,serif;font-weight:400;font-size:28px;line-height:31px;letter-spacing:2px;color:#fff}
.hero-lead{left:102px;top:130px;width:440px;font-family:"Raleway",sans-serif;font-size:11px;line-height:21px;color:#3a2a10;text-transform:uppercase}
.hero-sign{left:102px;top:214px;font-family:"Raleway",sans-serif;font-weight:600;font-size:11px;color:#fff}
.hero-name{left:102px;top:257px;font-family:"Raleway",sans-serif;font-size:12px;color:#3a2a10;text-transform:uppercase}
.contact-strip{left:0;top:425px;width:1047px;height:81px;background:var(--strip-bg);border-bottom:1px solid #d2d2d2}
.strip-pointer{left:467px;top:425px;width:0;height:0;border-left:9px solid transparent;border-right:9px solid transparent;border-top:9px solid #d49238}
.call-ring{left:98px;top:438px}
.call-text{left:120px;top:449px;font-family:"Open Sans",sans-serif;color:#666;font-size:16px;font-weight:600;line-height:20px}
.call-text small{font-size:12px}
.call-text .mail{font-size:14px;font-weight:400;display:block}
.thumb{top:439px;width:122px;height:54px;border:2px solid #fff}
.section-tag{left:97px;top:532px;width:185px;height:35px;background:linear-gradient(#e69b43,#d0802c);border-left:4px solid #8a5a20;font-family:"Open Sans",sans-serif;font-size:19px;color:#fff;padding:2px 0 0 14px;box-shadow:0 2px 3px rgba(0,0,0,.25)}
.section-tag span{color:#7a4f1a}
.source{left:440px;top:548px;font-size:10px;font-style:italic;color:#666}
.source b{font-style:normal;color:#333}
.intro-text{left:98px;top:583px;width:548px;font-size:10.6px;line-height:17.5px;letter-spacing:.3px;color:#444}
.newsletter-title{left:675px;top:525px;font-family:"Oswald",sans-serif;font-weight:400;font-size:24px;color:#333}
.newsletter-box{left:669px;top:560px;width:273px;height:100px;border:1px solid #ddd;border-radius:4px;box-shadow:0 1px 3px rgba(0,0,0,.1);background:#fff}
.newsletter-box p{position:absolute;left:22px;top:18px;font-size:12px;color:#444}
.newsletter-box .field{position:absolute;left:20px;top:52px;width:172px;height:26px;border:1px solid #ccc;font-size:12px;color:#666;padding:5px 8px}
.newsletter-box .go{position:absolute;left:201px;top:52px;width:47px;height:26px;background:#6b6b6b;border-radius:3px;color:#fff;font-size:13px;text-align:center;line-height:26px}
.services{left:0;top:712px;width:1047px;height:216px;background:var(--soft-bg);border-top:1px solid #e0e0e0}
.services-title{left:118px;top:735px;font-family:"Roboto Condensed",sans-serif;font-weight:700;font-size:24px;color:#444;display:flex;align-items:center;gap:8px}
.services-rule{left:118px;top:773px;width:468px;height:1px;background:#c8c8c8}
.services-text{left:118px;top:785px;width:470px;font-family:"Roboto Condensed",sans-serif;font-size:14.5px;line-height:21px;color:#555;text-align:justify}
.services-text .site{color:var(--orange-text);font-size:16px;margin-right:18px}
.services-text .link{color:var(--orange-text);text-decoration:underline}
.read-more{left:120px;top:886px;font-family:"Roboto Condensed",sans-serif;font-weight:700;font-size:14px;color:#e8a03a;border-bottom:2px dashed #e8a03a;padding-bottom:2px}
.video{left:605px;top:738px;width:332px;height:163px;background:#fff;padding:4px;box-shadow:0 1px 3px rgba(0,0,0,.2)}
.video-still{width:100%;height:100%;background:linear-gradient(90deg,#b9d6c3 0%,#e7eeea 45%,#cfd6da 100%);position:relative}
.video-bar{position:absolute;left:8px;bottom:8px;width:308px;height:20px;background:#2a2a2a;border-radius:2px}
.site-footer{left:0;top:928px;width:1047px;height:234px;background:var(--footer-bg)}
.foot-brand{left:94px;top:962px;font-family:"Libre Baskerville",Georgia,serif;font-size:18px;line-height:20px;color:#bdbdbd;display:flex;align-items:center;gap:8px}
.foot-brand i{width:12px;height:12px;background:#8a8a8a;display:block}
.foot-brand small{display:block;font-size:15px}
.foot-contact{left:100px;top:1020px;font-size:11px;line-height:14px;color:#ddd}
.foot-row{position:absolute;left:0;display:flex;gap:10px;white-space:nowrap}
.foot-map{left:301px;top:973px;width:222px;height:139px;border:3px solid #999;background:linear-gradient(135deg,#e9e6e1,#d9d6d0)}
.foot-col h3{font-family:"Open Sans",sans-serif;font-weight:600;font-size:15px;color:#eee;margin-bottom:8px}
.foot-nav{left:578px;top:970px}
.foot-nav li{list-style:none;font-size:11.5px;line-height:20px;color:#ccc}
.foot-social{left:772px;top:970px}
.foot-social li{list-style:none;display:flex;align-items:center;gap:6px;font-size:11px;color:#bbb;height:32px}
.foot-social li span{width:26px;height:26px;border-radius:50%;background:#111;display:block}
.bottom-bar{left:0;top:1162px;width:1047px;height:38px;background:var(--bottom-bg);color:#fff;font-size:11px;padding:12px 0 0 101px}
</style>
</head>
<body>

<header class="site-header abs">
  <div class="brand abs"><span class="brand-mark"></span><div>TIVARELCAP<small>Zahnarztpraxis</small></div></div>
  <div class="social-top abs"><span></span><span></span><span></span><span></span></div>
  <nav class="main-nav abs">
    <a class="active">HOME</a><a>ZAHNMEDIZIN</a><a>DENTALHYGEINE</a><a>TEAM</a><a>KONTAKT</a>
  </nav>
</header>

<section class="hero abs">
  <div class="hero-photo abs" role="img" aria-label="Smiling woman resting her chin on her hands"></div>
  <h1 class="hero-title abs">Herzlich willkommen<br>unserer neuen Praxis.</h1>
  <p class="hero-lead abs">Es ist unser Ziel, Ihr Wohlbefinden zu steigern. Sie sollen die Schön­heit des Alltags mit gesunden Zähnen geniessen und in jeder Situa­tion herzhaft lachen können.</p>
  <p class="hero-sign abs">IHRE ZAHNÄRZTIN</p>
  <p class="hero-name abs">Dr. med. dent. Lena Marquardt-Vogel</p>
</section>

<section class="contact-strip abs"></section>
<div class="strip-pointer abs"></div>
<svg class="call-ring abs" width="56" height="56" viewBox="0 0 56 56"><path d="M44 12 A23 23 0 1 0 44 44" fill="none" stroke="#9a9a9a" stroke-width="4" stroke-dasharray="8 5"/></svg>
<div class="call-text abs">Call: 1-800-555-0187 <small>(Toll Free)</small><span class="mail">Email:info@tivarel.ch</span></div>
<div class="thumb abs" style="left:412px;background:linear-gradient(135deg,#f0c060,#d89a3c)" role="img" aria-label="Doctor in scrubs"></div>
<div class="thumb abs" style="left:547px;background:linear-gradient(135deg,#c9ccd0,#8d939a)" role="img" aria-label="Medical team"></div>
<div class="thumb abs" style="left:681px;background:linear-gradient(135deg,#6a5a55,#b5a090)" role="img" aria-label="Graduates in caps"></div>
<div class="thumb abs" style="left:815px;background:linear-gradient(135deg,#7fa7a0,#b08a78)" role="img" aria-label="Surgical staff"></div>

<div class="section-tag abs"><span>What is</span> Dentistry?</div>
<p class="source abs">▸ From <b>Openpedia</b>, the free encyclopedia</p>
<p class="intro-text abs">Ipsum is simply dummy text of the printing and typesetting industry. Lorem Ipsum has been the industry's standard dummy text ever since the 1500s, when an unknown printer took a galley of type and scrambled it to make a type specimen book. It has survived not only five centuries, but also the leap into electronic typesetting, remaining essentially unchanged. It was popularised in the 1960s with the release of Inkform sheets containing Lorem Ipsum passages, and more recently with.</p>

<h2 class="newsletter-title abs">Newsletter</h2>
<div class="newsletter-box abs">
  <p>Sign up our newsletter to get latest updates</p>
  <div class="field">Email Address</div>
  <div class="go">GO</div>
</div>

<section class="services abs"></section>
<h2 class="services-title abs">
  <svg width="26" height="24" viewBox="0 0 26 24"><circle cx="9" cy="13" r="6" fill="none" stroke="#555" stroke-width="4" stroke-dasharray="3 2"/><circle cx="20" cy="6" r="4" fill="none" stroke="#555" stroke-width="3" stroke-dasharray="2 1.5"/></svg>What We Do</h2>
<div class="services-rule abs"></div>
<p class="services-text abs"><span class="site">tivarel.ch</span> convallis libero, ut accumsan risus gravida in. Vivamus vehicula et magna non tincidunt. Aliquam <span class="link">placerat massa sed</span> est lobortis viverra. Mauris sit amet sagittis erat. Sed tempus nisl felis, at aliquet odio pellentesque a. Proin dolor ligula, lobortis ac egestas id, varius non erat.</p>
<div class="read-more abs">Read More ➜</div>
<div class="video abs">
  <div class="video-still" role="img" aria-label="Video still of a doctor holding a tablet">
    <div class="video-bar"><svg width="308" height="20"><rect x="3" y="2" width="34" height="16" fill="#444"/><path d="M16 6 L24 10 L16 14Z" fill="#fff"/><rect x="48" y="8" width="230" height="4" fill="#555"/><rect x="48" y="8" width="60" height="4" fill="#2f9ad6"/></svg></div>
  </div>
</div>

<footer class="site-footer abs"></footer>
<div class="foot-brand abs"><i></i><div>TIVARELCAP<small>Zahnarztpraxis</small></div></div>
<div class="foot-contact abs">
  <div class="foot-row" style="top:0">
    <svg width="22" height="20" viewBox="0 0 22 20"><path d="M11 1 L21 10 H18 V19 H13 V13 H9 V19 H4 V10 H1Z" fill="#ccc"/></svg>
    <span>Meridian Learning Co.<br>12 Harbour Lane<br>Ashford, ON K2P 1L7</span></div>
  <div class="foot-row" style="top:54px;font-size:12.5px">
    <svg width="22" height="14" viewBox="0 0 22 14"><path d="M1 5 Q11 -3 21 5 L18 8 L15 6 V4 H7 V6 L4 8Z M6 8 H16 L18 13 H4Z" fill="#ccc"/></svg>
    <span>1-800-555-0187 <small style="font-size:11px">(Toll Free)</small></span></div>
  <div class="foot-row" style="top:80px;font-size:12.5px">
    <svg width="22" height="14" viewBox="0 0 22 14"><rect x="1" y="1" width="20" height="12" fill="none" stroke="#ccc" stroke-width="1.5"/><path d="M1 1 L11 8 L21 1" fill="none" stroke="#ccc" stroke-width="1.5"/></svg>
    <span>info@tivarel.ch</span></div>
</div>
<div class="foot-map abs" role="img" aria-label="Street map of the practice location"></div>
<div class="foot-col foot-nav abs">
  <h3>Footer Navigation</h3>
  <ul><li>› Home</li><li>› Privacy Policy</li><li>› Terms &amp; Conditions</li><li>› Acceptance Chart</li><li>› FAQ</li></ul>
</div>
<div class="foot-col foot-social abs">
  <h3>Socialize with us</h3>
  <ul><li><span></span>LIKE US ON FRIENDBOOK</li><li><span></span>FOLLOW US ON CHIRPER</li><li><span></span>CONNECT US ON CIRCLESPACE</li></ul>
</div>
<div class="bottom-bar abs">Copyright 2014 Tivarelcap. All Rights Reserved</div>

</body>
</html>
```